VORNAX Technologies Catalogue Design

We want the existing catalogue design to be completely re designed to have a better theme, that is professional and dynamic. we want the existing pictures changed, it would be great to have some images of local UAE population engaging in the activities shown. most of the written content remains the same. No.1 what we believe is to be removed. Point No. 3 all the little logos need to be re designed.

Target Market(s)

residential and corporate clients

Industry/Entity Type

home automation, command centers, audio video systems, lighting control systems

Requirements
Must have
• Point No. 3 all the little logos need to be re designed. Overall theme of the catalogue should look very good.
Nice to have
• Good font. Color theme can be related to logo which is black grey and red. Red maybe little less, leaving it to the designer to decide. it would be nice to have the cover of the catalogue clean and elegant. I have added doc of a pattern in blue color, it would be nice if it can be used as theme in the entire catalogue either in grey or black color, not blue.

```html
<!DOCTYPE html>
<html lang="en">
<head>
<meta charset="utf-8">
<title>VORNAX Technologies Catalogue</title>
<link rel="stylesheet" href="https://fonts.googleapis.com/css2?family=Montserrat:wght@300;400;500;600;700;800&display=swap">
<style>
:root{
  --red:#e3192a;
  --ink:#1f1f1f;
  --charcoal:#2e2e2e;
  --slate:#3c3c3c;
  --steel:#4d4d4d;
  --mist:#9a9a9a;
  --paper:#ffffff;
  --stage-top:#cbcbcb;
  --stage-bottom:#dedede;
  --body-grey:#6b6b6b;
}
*{margin:0;padding:0;box-sizing:border-box}
html,body{width:1200px;height:2626px;overflow:hidden}
body{
  position:relative;
  font-family:"Montserrat",Arial,sans-serif;
  background:linear-gradient(180deg,var(--stage-top),var(--stage-bottom) 50%,var(--stage-top));
  color:var(--ink);
}
.page{position:absolute;overflow:hidden;box-shadow:0 4px 14px rgba(0,0,0,.35)}

/* ---------- cover ---------- */
.cover{left:155px;top:87px;width:827px;height:1068px;background:var(--paper)}
.cover-art{position:absolute;left:0;top:0}
.brand{position:absolute;left:130px;top:62px;display:flex;align-items:center;gap:26px}
.brand-mark{width:120px;height:120px;border-radius:50%;background:var(--red)}
.brand-name{font-weight:800;color:var(--ink);line-height:1}
.brand-name .primary{display:block;font-size:88px;letter-spacing:10px}
.brand-name .secondary{display:block;font-size:31px;letter-spacing:3px;margin-top:10px}
.cover-title{position:absolute;left:0;width:100%;top:826px;text-align:center;color:#fff;font-size:33px;font-weight:700;letter-spacing:.5px}
.cover-rule{position:absolute;left:188px;top:876px;width:451px;height:7px;
  background:linear-gradient(90deg,#fff 0 42%,#cfcfcf 42% 72%,#b8b8b8 72%)}
.cover-lede{position:absolute;left:160px;width:507px;top:913px;text-align:center;color:#f2f2f2;font-size:16px;font-weight:300;line-height:1.2}

/* ---------- about ---------- */
.about{left:60px;top:1201px;width:509px;height:658px;background:var(--paper)}
.about-photo{position:absolute;left:0;top:0;width:100%;height:245px;
  background:
    radial-gradient(ellipse 90px 80px at 48% 40%,rgba(246,212,150,.95) 0,rgba(214,170,110,.55) 45%,rgba(214,170,110,0) 100%),
    linear-gradient(180deg,rgba(255,255,255,0) 0 68%,rgba(236,238,242,.95) 84%,#f4f5f7 100%),
    linear-gradient(90deg,#8d949c 0,#5d646c 14%,#24262b 32%,#1d1e22 60%,#34373c 78%,#a9aeb4 100%)}
.about-banner{position:absolute;left:0;top:245px;width:100%;height:45px;background:var(--red);color:#fff;
  text-align:center;font-size:29px;font-weight:400;line-height:45px;letter-spacing:.5px}
.about-banner b{font-weight:700}
.about-intro{position:absolute;left:0;top:290px;width:100%;height:133px;background:var(--slate);padding:18px 30px 0;
  color:#cfcfcf;font-size:7.4px;line-height:1.25;text-align:center}
.about-intro p{margin-bottom:8px}
.team-title{position:absolute;left:39px;top:449px;color:var(--red);font-size:20px;font-weight:800;line-height:1.15}
.team-copy{position:absolute;left:39px;top:500px;width:226px;font-size:9px;font-weight:600;line-height:1.2;text-align:justify;color:var(--ink)}
.team-copy p{margin-bottom:9px}
.team-halo{position:absolute;left:289px;top:460px;width:168px;height:160px;border-radius:50%;background:#e4e8f2}
.team-photo{position:absolute;left:302px;top:443px;width:160px;height:196px;border-radius:50%;
  background:
    radial-gradient(ellipse 34px 56px at 52% 52%,#6fa3de 0,#4f86c6 55%,rgba(79,134,198,0) 100%),
    linear-gradient(90deg,#e9ecef 0,#c9ced3 35%,#8f949a 60%,#d8dbde 100%)}

/* ---------- services ---------- */
.services{left:630px;top:1201px;width:510px;height:658px;
  background:linear-gradient(135deg,#555 0%,#3f3f3f 50%,#4a4a4a 100%)}
.services-title{position:absolute;left:155px;top:22px;color:#fff;font-size:26px;font-weight:400;letter-spacing:.5px}
.services-title b{font-weight:700}
.services-rule{position:absolute;left:155px;top:63px;width:199px;height:2px;background:#fff}
.service{position:absolute;left:51px;width:420px;border-left:2px solid #e0e0e0;padding-left:16px}
.service::before{content:"";position:absolute;left:0;top:0;width:58px;height:2px;background:#e0e0e0}
.service h3{font-size:16px;font-weight:700;color:#fff;letter-spacing:.5px;padding-top:12px;margin-bottom:8px}
.service h3 .accent{color:var(--red)}
.service p{width:300px;font-size:7.6px;line-height:1.38;color:#e8e8e8;margin-bottom:8px}
.service-icon{position:absolute;left:340px}

/* ---------- solutions ---------- */
.solutions{left:342px;top:1911px;width:508px;height:658px;background:var(--paper)}
.solutions-title{position:absolute;left:37px;top:36px;font-size:23px;font-weight:800;color:var(--ink)}
.solutions-title .accent{color:var(--red)}
.solutions-rule{position:absolute;left:261px;top:50px;width:219px;height:2px;background:#555}
.tag{position:absolute;display:flex;height:21px}
.tag-stripes{width:38px;height:21px;
  background:repeating-linear-gradient(60deg,var(--red) 0 4px,transparent 4px 8px)}
.tag-label{margin-left:-4px;background:var(--charcoal);color:#fff;font-size:12.5px;font-weight:600;letter-spacing:1px;
  line-height:21px;padding:0 26px 0 12px;clip-path:polygon(10px 0,100% 0,calc(100% - 10px) 100%,0 100%)}
.solution-copy{position:absolute;width:235px;font-size:7.4px;line-height:1.2;color:var(--body-grey);text-align:justify}
.solution-photo{position:absolute;width:166px;height:115px}
.photo-network{background:
  radial-gradient(ellipse 60px 14px at 45% 12%,rgba(226,70,60,.75) 0,rgba(226,70,60,0) 100%),
  linear-gradient(165deg,#2a2d33 0,#15171b 45%,#3b2420 80%,#6a2d22 100%)}
.photo-command{background:
  radial-gradient(ellipse 40px 50px at 58% 62%,#e9eef4 0,rgba(233,238,244,0) 100%),
  linear-gradient(135deg,#15345c 0,#2f6aa6 45%,#6fa4d4 75%,#a9c4dc 100%)}
.photo-hall{background:
  radial-gradient(ellipse 70px 30px at 50% 30%,rgba(250,214,160,.8) 0,rgba(250,214,160,0) 100%),
  linear-gradient(180deg,#8a5a34 0,#d19458 40%,#b06a38 70%,#5a2f1e 100%)}
.corner{position:absolute;width:30px;height:30px;border-color:var(--red);border-style:solid;border-width:0}
.corner.br{border-right-width:2px;border-bottom-width:2px}
.corner.bl{border-left-width:2px;border-bottom-width:2px}
.skyline{position:absolute;left:15px;top:530px;width:478px;height:80px;
  background:linear-gradient(180deg,rgba(40,40,40,0) 0%,rgba(40,40,40,.55) 40%,#2a2a2a 100%)}
.contact-bar{position:absolute;left:0;top:609px;width:100%;height:25px;background:var(--charcoal);
  display:flex;align-items:center;color:#fff;font-size:10.5px;font-weight:600}
.contact-bar span{flex:1;text-align:center}
.contact-bar span+span{border-left:1px solid #fff}
.site{position:absolute;left:0;top:640px;width:100%;text-align:center;font-size:10.5px;font-weight:700;color:var(--ink)}
</style>
</head>
<body>

<!-- Cover -->
<section class="page cover">
  <svg class="cover-art" width="827" height="1068" viewBox="0 0 827 1068">
    <defs>
      <linearGradient id="band" x1="0" y1="0" x2="1" y2="0">
        <stop offset="0" stop-color="#5c5c5c"/>
        <stop offset=".55" stop-color="#6e6e6e"/>
        <stop offset="1" stop-color="#a2a2a2"/>
      </linearGradient>
      <linearGradient id="veil" x1="0" y1="0" x2="1" y2="1">
        <stop offset="0" stop-color="#fff" stop-opacity=".9"/>
        <stop offset="1" stop-color="#fff" stop-opacity=".15"/>
      </linearGradient>
      <linearGradient id="techBase" x1="0" y1="0" x2="0" y2="1">
        <stop offset="0" stop-color="#2b2c31"/>
        <stop offset=".55" stop-color="#1e1f23"/>
        <stop offset=".8" stop-color="#6a6d72"/>
        <stop offset="1" stop-color="#e9ebee"/>
      </linearGradient>
      <linearGradient id="techWindow" x1="0" y1="0" x2="1" y2="0">
        <stop offset="0" stop-color="#a3a9af" stop-opacity=".9"/>
        <stop offset=".22" stop-color="#5d6269" stop-opacity=".4"/>
        <stop offset=".4" stop-color="#000" stop-opacity="0"/>
      </linearGradient>
      <radialGradient id="techGlow" cx=".5" cy=".55" r=".32">
        <stop offset="0" stop-color="#fbe0a8"/>
        <stop offset=".35" stop-color="#d9a766" stop-opacity=".7"/>
        <stop offset="1" stop-color="#d9a766" stop-opacity="0"/>
      </radialGradient>
      <linearGradient id="rack" x1="0" y1="0" x2="1" y2="1">
        <stop offset="0" stop-color="#e6e8eb"/>
        <stop offset=".35" stop-color="#b4bac1"/>
        <stop offset=".6" stop-color="#3f84c4"/>
        <stop offset="1" stop-color="#26303c"/>
      </linearGradient>
      <radialGradient id="phone" cx=".55" cy=".5" r=".55">
        <stop offset="0" stop-color="#4f8bd0"/>
        <stop offset=".4" stop-color="#7fa6d4"/>
        <stop offset="1" stop-color="#e4e7ea"/>
      </radialGradient>
    </defs>
    <rect x="0" y="632" width="827" height="436" fill="url(#band)"/>
    <polygon points="560,1068 827,632 827,1068" fill="#fff" opacity=".08"/>
    <g role="img" aria-label="Photo: professional working at a desk with a glowing digital network overlay">
      <polygon points="268,265 559,265 696,512 559,759 268,759 125,512" fill="url(#techBase)"/>
      <polygon points="268,265 559,265 696,512 559,759 268,759 125,512" fill="url(#techWindow)"/>
      <polygon points="268,265 559,265 696,512 559,759 268,759 125,512" fill="url(#techGlow)"/>
    </g>
    <polygon points="727,451 766,374 827,374 827,529 766,529" fill="url(#veil)"/>
    <polygon points="579,612 622,525 722,525 722,698 622,698" fill="url(#veil)" opacity=".6"/>
    <polygon points="503,343 560,229 697,229 754,343 697,458 560,458" fill="url(#rack)" stroke="#e3192a" stroke-width="14" stroke-linejoin="miter" role="img" aria-label="Photo: technician crimping network cables at a patch panel"/>
    <polygon points="100,705 148,614 246,614 294,705 246,797 148,797" fill="url(#phone)" stroke="#fff" stroke-width="6" role="img" aria-label="Photo: hand holding a smartphone with a home automation app"/>
    <polygon points="21,913 44,874 88,874 111,913 88,953 44,953" fill="url(#veil)" opacity=".45"/>
    <polygon points="43,980 77,921 145,921 179,980 145,1040 77,1040" fill="url(#veil)" opacity=".6"/>
  </svg>

  <div class="brand">
    <span class="brand-mark"></span>
    <div class="brand-name"><span class="primary">VORNAX</span><span class="secondary">TECHNOLOGIES L.L.C</span></div>
  </div>

  <h1 class="cover-title">LOREM IPSUM DOLOR</h1>
  <div class="cover-rule"></div>
  <p class="cover-lede">Lorem ipsum dolor sit amet, consectetur adipiscing elit, sed do eiusmod tempor incididunt ut labore et dolore magna aliqua. Ut e ni m ad mini mv eniam,</p>
</section>

<!-- About -->
<section class="page about">
  <div class="about-photo" role="img" aria-label="Photo: businessman at a desk with tablet, laptop and a glowing network overlay, city window behind"></div>
  <h2 class="about-banner">EVERYTHING <b>ABOUT US</b></h2>
  <div class="about-intro">
    <p>WE, Vornax Technologies, strive for Customer Satisfaction, with a Technology Touch.</p>
    <p>Vornax Technologies is part of well-known Vornax Group established in the year 1999. Vornax Group has grown organically expanding its portfolio spread across multi segments.</p>
    <p>Vornax belongs to a Group which primarily promotes trade and commerce through its affiliation with several large multi- national entities. By virtue of its status as agent and partner, the Group provides opportunities to a global network of venture's seeking business opportunities in the region. Further, the Group's extensive knowledge of UAE's industrial and commercial infrastructure as well as in the Middle East at large makes it an ideal business partner offering comprehensive benefits in a wide range of products &amp; services.</p>
  </div>
  <h2 class="team-title">OUR EXCEPTIONAL<br>TEAM</h2>
  <div class="team-copy">
    <p>Our biggest strength is our high-performance team of thoroughly chosen professionals with proven expertise in soil, water, wildlife, and vegetation assessments, contamination management and remediation, spill response, regulatory approvals, and regulatory closure.</p>
    <p>Since the inception of Astrel in 2014, our team has successfully completed a truly wide range of exciting projects for our Clients. We incorporate creativity, practicality, and problem-solving into all our projects.</p>
  </div>
  <div class="team-halo"></div>
  <div class="team-photo" role="img" aria-label="Photo: hand holding a smartphone showing a smart home app"></div>
</section>

<!-- Services -->
<section class="page services">
  <h2 class="services-title">OUR <b>SERVICES</b></h2>
  <div class="services-rule"></div>

  <article class="service" style="top:90px">
    <h3>HOME &amp; OFFICE <span class="accent">AUTOMATION</span></h3>
    <p>Lorem ipsum dolor sit amet, consectetuer adipiscing elit, sed diam nonummy nibh euismod tincidunt ut laoreet dolore magna aliquam erat volutpat. Ut wisi enim ad minim veniam, quis nostrud exerci tation ullamcorper suscipit lobortis nisl ut aliquip ex ea commodo consequat. Duis autem vel eum iriure dolor in hendrerit in vulputate velit esse molestie consequat, vel illum dolore.</p>
    <svg class="service-icon" style="top:18px" width="84" height="74" viewBox="0 0 84 74" aria-hidden="true">
      <circle cx="42" cy="36" r="30" fill="#e3192a"/>
      <circle cx="8" cy="10" r="6" fill="#fff"/><circle cx="76" cy="10" r="6" fill="#fff"/><circle cx="40" cy="68" r="6" fill="#fff"/>
      <text x="42" y="43" text-anchor="middle" fill="#fff" font-family="Montserrat,Arial,sans-serif" font-size="20" font-weight="600">CO₂</text>
    </svg>
  </article>

  <article class="service" style="top:209px">
    <h3><span class="accent">AV</span> DISTRIBUTION &amp; HOME CINEMA</h3>
    <p>Lorem ipsum dolor sit amet, consectetuer adipiscing elit, sed diam nonummy nibh euismod tincidunt ut laoreet dolore magna aliquam erat volutpat. Ut wisi enim ad minim veniam, quis nostrud exerci tation ullamcorper suscipit lobortis nisl ut aliquip ex ea commodo consequat. Duis autem vel eum iriure dolor in hendrerit in vulputate velit esse molestie consequat, vel illum dolore.</p>
    <p>Lorem ipsum dolor sit amet, consectetuer adipiscing elit, sed diam nonummy nibh euismod tincidunt ut laoreet dolore magna aliquam erat volutpat. Ut wisi enim ad</p>
    <svg class="service-icon" style="top:26px;left:344px" width="76" height="70" viewBox="0 0 76 70" aria-hidden="true">
      <path d="M38 6 L56 38 L46 38 L38 24 L30 38 L20 38 Z" fill="#fff"/>
      <path d="M60 44 L72 64 L40 64 L40 54 L58 54 Z" fill="#e3192a"/>
      <path d="M16 44 L4 64 L34 64 L34 54 L18 54 Z" fill="#e3192a"/>
    </svg>
  </article>

  <article class="service" style="top:361px">
    <h3>GRMS &amp; LIGHTING <span class="accent">CONTROL</span></h3>
    <p>Lorem ipsum dolor sit amet, consectetuer adipiscing elit, sed diam nonummy nibh euismod tincidunt ut laoreet dolore magna aliquam erat volutpat. Ut wisi enim ad minim veniam, quis nostrud exerci tation ullamcorper suscipit lobortis nisl ut aliquip ex ea commodo consequat. Duis autem vel eum iriure dolor in hendrerit in vulputate velit esse molestie consequat, vel illum dolore eu feugiat nulla facilisis at vero eros et accumsan et iusto odio dignissim qui blandit praesent luptatum zzril delenit augue duis dolore te feugait nulla facilisi.</p>
    <svg class="service-icon" style="top:-16px;left:348px" width="72" height="96" viewBox="0 0 72 96" aria-hidden="true">
      <circle cx="50" cy="12" r="9" fill="#fff"/><circle cx="40" cy="20" r="7" fill="#fff"/><circle cx="58" cy="22" r="6" fill="#fff"/>
      <rect x="40" y="30" width="16" height="24" fill="#e3192a"/>
      <rect x="4" y="54" width="64" height="38" fill="#fff"/>
      <rect x="40" y="54" width="16" height="38" fill="#e3192a"/>
      <rect x="12" y="64" width="5" height="4" fill="#4a4a4a"/><rect x="22" y="64" width="5" height="4" fill="#4a4a4a"/>
      <rect x="12" y="76" width="5" height="4" fill="#4a4a4a"/><rect x="22" y="76" width="5" height="4" fill="#4a4a4a"/>
    </svg>
  </article>

  <article class="service" style="top:504px">
    <h3><span class="accent">EMERGING</span> TECHNOLOGIES</h3>
    <p>Lorem ipsum dolor sit amet, consectetuer adipiscing elit, sed diam nonummy nibh euismod tincidunt ut laoreet dolore magna aliquam erat volutpat. Ut wisi enim ad minim veniam, quis nostrud exerci tation ullamcorper suscipit lobortis nisl ut aliquip ex ea commodo consequat. Duis autem vel eum iriure dolor in hendrerit in vulputate velit esse molestie consequat, vel illum dolore.</p>
    <svg class="service-icon" style="top:6px;left:354px" width="62" height="86" viewBox="0 0 62 86" aria-hidden="true">
      <path d="M31 2 C31 2 2 40 2 56 A29 29 0 0 0 60 56 C60 40 31 2 31 2 Z" fill="#fff"/>
      <circle cx="31" cy="60" r="12" fill="#e3192a"/>
    </svg>
  </article>
</section>

<!-- Solutions -->
<section class="page solutions">
  <h2 class="solutions-title">OUR <span class="accent">SOLUTIONS</span></h2>
  <div class="solutions-rule"></div>

  <div class="tag" style="left:43px;top:89px"><span class="tag-stripes"></span><span class="tag-label">ELV &amp; NETWORKING</span></div>
  <p class="solution-copy" style="left:43px;top:128px">Lorem ipsum dolor sit amet, consectetuer adipiscing elit, sed diam nonummy nibh euismod tincidunt ut laoreet dolore magna aliquam erat volutpat. Ut wisi enim ad minim veniam, quis nostrud exerci tation ullamcorper suscipit lobortis nisl ut aliquip ex ea commodo consequat. Duis autem vel eum iriure dolor in hendrerit in vulputate velit esse molestie consequat, vel illum dolore eu feugiat nulla facilisis at vero eros et accumsan et iusto odio dignissim qui blandit praesent luptatum zzril delenit augue</p>
  <div class="solution-photo photo-network" style="left:306px;top:87px" role="img" aria-label="Photo: close-up of network cables plugged into a switch with red status lights"></div>
  <span class="corner br" style="left:450px;top:180px"></span>

  <div class="tag" style="left:237px;top:238px"><span class="tag-stripes"></span><span class="tag-label">COMMAND CENTER</span></div>
  <p class="solution-copy" style="left:237px;top:277px">Lorem ipsum dolor sit amet, consectetuer adipiscing elit, sed diam nonummy nibh euismod tincidunt ut laoreet dolore magna aliquam erat volutpat. Ut wisi enim ad minim veniam, quis nostrud exerci tation ullamcorper suscipit lobortis nisl ut aliquip ex ea commodo consequat. Duis autem vel eum iriure dolor in hendrerit in vulputate velit esse molestie consequat, vel illum dolore eu feugiat nulla facilisis at vero eros et accumsan et iusto</p>
  <div class="solution-photo photo-command" style="left:45px;top:235px" role="img" aria-label="Photo: operator at a command center desk facing wall monitors with world maps"></div>
  <span class="corner bl" style="left:36px;top:331px"></span>

  <div class="tag" style="left:43px;top:389px"><span class="tag-stripes"></span><span class="tag-label">ENTERTAINMENT</span></div>
  <p class="solution-copy" style="left:43px;top:426px">Lorem ipsum dolor sit amet, consectetuer adipiscing elit, sed diam nonummy nibh euismod tincidunt ut laoreet dolore magna aliquam erat volutpat. Ut wisi enim ad minim veniam, quis nostrud exerci tation ullamcorper suscipit lobortis nisl ut aliquip ex ea commodo consequat. Duis autem vel eum iriure dolor in hendrerit in vulputate velit esse molestie consequat, vel illum dolore eu feugiat nulla facilisis at vero eros et accumsan et iusto odio dignissim qui blandit praesent luptatum zzril delenit augue</p>
  <div class="solution-photo photo-hall" style="left:306px;top:384px" role="img" aria-label="Photo: warm-lit concert hall with wooden stage and seating"></div>
  <span class="corner br" style="left:450px;top:476px"></span>

  <div class="skyline" role="img" aria-label="Illustration: city skyline silhouette with trees, wind turbines and clouds"></div>
  <div class="contact-bar">
    <span>1-555-204-7310</span>
    <span>info@vornaxtech.example</span>
    <span>555-318-6402</span>
  </div>
  <p class="site">www.vornaxtech.example</p>
</section>

</body>
</html>
```